Business Card Design

Massage therapy and healthy food
Zenlo Health Massage (business name)

Target Market(s)

Health conscious

Industry/Entity Type

Business

Contact Information for Business Card

0413867205

Font styles to use
Serif

```html
<!DOCTYPE html>
<html lang="en">
<head>
<meta charset="utf-8">
<title>Zenlo Health Massage — Business Card</title>
<link rel="stylesheet" href="https://fonts.googleapis.com/css2?family=Arimo:wght@400;700&display=swap">
<style>
  :root {
    --backdrop: #e9e4de;
    --card-black: #0b0a0c;
    --card-black-sheen: #2a282c;
    --orchid: #c35fd6;
    --orchid-light: #d77ae6;
    --orchid-deep: #a646bd;
    --text-white: #ffffff;
    --text-dark: #1a1020;
  }
  * { margin: 0; padding: 0; box-sizing: border-box; }
  html, body { width: 1200px; height: 902px; overflow: hidden; }
  body {
    background: var(--backdrop);
    font-family: "Arimo", Arial, sans-serif;
    position: relative;
  }
  .card {
    position: absolute;
    width: 530px;
    height: 303px;
    border-radius: 4px;
    overflow: hidden;
    box-shadow: 0 10px 28px rgba(0,0,0,0.25);
    background: linear-gradient(150deg, var(--card-black-sheen) 0%, var(--card-black) 45%, var(--card-black) 100%);
  }
  .card-front { left: 40px; top: 300px; }
  .card-back { left: 630px; top: 300px; }

  .brand { display: flex; align-items: center; gap: 12px; }
  .brand-dot {
    width: 22px; height: 22px; border-radius: 50%;
    background: var(--orchid-light);
    flex: none;
  }
  .brand-name {
    color: var(--text-white);
    font-weight: 400;
    white-space: nowrap;
  }
  .card-front .brand {
    position: absolute; left: 0; right: 0; top: 128px;
    justify-content: center;
  }
  .card-front .brand-name { font-size: 34px; }

  .band {
    position: absolute; left: 0; right: 0;
    background: linear-gradient(90deg, var(--orchid-deep), var(--orchid) 55%, var(--orchid-light));
  }
  .band-top { top: 0; height: 68px; }
  .band-bottom { bottom: 0; height: 46px; }
  .tagline {
    position: absolute; left: 26px; top: 28px;
    color: var(--text-dark);
    font-size: 15px;
  }
  .card-back .brand {
    position: absolute; left: 28px; top: 158px;
  }
  .card-back .brand-dot { width: 16px; height: 16px; }
  .card-back .brand-name { font-size: 21px; }
  .divider {
    position: absolute; left: 318px; top: 90px;
    width: 1px; height: 144px;
    background: var(--orchid);
  }
  .contact {
    position: absolute; left: 342px; top: 104px;
    color: var(--text-white);
  }
  .employee-name { font-size: 24px; font-weight: 400; }
  .employee-title { font-size: 12px; margin: 4px 0 0 68px; }
  .phone { font-size: 20px; margin-top: 38px; letter-spacing: 0.5px; }
</style>
</head>
<body>
  <section class="card card-front" aria-label="Card front">
    <div class="brand">
      <span class="brand-dot"></span>
      <span class="brand-name">Zenlo Health Massage</span>
    </div>
  </section>

  <section class="card card-back" aria-label="Card back">
    <div class="band band-top"></div>
    <p class="tagline">Massage therapy and healthy food</p>
    <div class="brand">
      <span class="brand-dot"></span>
      <span class="brand-name">Zenlo Health Massage</span>
    </div>
    <div class="divider"></div>
    <div class="contact">
      <p class="employee-name">Employee name</p>
      <p class="employee-title">Your Title</p>
      <p class="phone">0413867205</p>
    </div>
    <div class="band band-bottom"></div>
  </section>
</body>
</html>
```